New design for our charity business cards

We are a small (but highly effective) suicide prevention charity in Australia looking to improve our brand. We recently rebranded in 2016 and have a new name and logo, but need new business cards designed. We are looking for something modern, bright, corporate, clean, cutting edge. It needs to work for the corporate sector, as thats to whom we are appealing for funding, but also to govt and public.

You have quite a free reign to design something cool, modern and a bit different. Use of logo is flexible - so show all or part, and get rid of or change the use of words underneath the logo. e.g. Drop second line (shown in grey) and just use name in one colour, or don't use name at all. Ok to use partial logo, for example ending off the card so its just strongly implied and not fully visible. Try us - we're looking for artistic!
Updates

Project Deadline Extended
Reason: Won't be able to complete this on 15th Aug so may as well give people more time for more designs. Many thanks.

Target Market(s)

Corporate funders, therefore large multinationals and govt. Want to convey strength and professionalism despite very small organisation behind the scenes.

Industry/Entity Type

Charity

Contact Information for Business Card

Gary Tolvern
CEO
Homeward Kin Circle
+61 (0)472 918254
gary.tolvern@homewardkincircle.com
www.homewardkincircle.com

Font styles to use
Sans Serif

Colors

Designer to choose colors to be used in the design.

Requirements
Must have
• Rear of card should list our organisational values and our address, so that the front is a cleaner, minimal design. Values (bolder) and address (subtle) are:
• One big family
• Sleep well at night
• Open heart, open mind
• If not us, who?
• Rock solid
• Do more with less
• PO Box 8471, Coffs Harbour, NSW 2450 Australia
• The values might be floating and in background, as long as legible. Use of different shades for the values could work too.
• If there is room, and putting too much on the back of the card is not a problem, then adding our strategy would be great as well. This is:
• Focus: Individual, Cultural, Systemic.
Nice to have
• Minimal colours, definitely the logo Ochra (colour of Australian earth) but then perhaps shades of grey to black only, alongside this.
• Am ok with having partial logo, meaning it goes off the card or use of just the curves - no need for entire logo to be displayed. The logo can be 'implied' if not fully displayed, but should be obviously branded as HKC due to enough of the logo showing. Happy for full logo to be showing too. Just want to give artists / designers free reign to go a bit funky, as far as thats possible with a corporate card!
• Please remove last grey line from logo if using whole logo, as that is now superfluous and not used. Also, the name 'Homeward Kin Circle' under the image of the logo can be one colour for a cleaner look - so either ochre to match logo of some greyscale.
Should not have
• Cannot have anything that is gender specific as we support mums, dads, kids, same sex parents - thats why our logo implies two parents and a child but the parents gender cannot be seen and the colours represent Australia (ochre soil) versus something that might be associated with a gender.

```html
<!DOCTYPE html>
<html lang="en">
<head>
<meta charset="utf-8">
<title>Homeward Kin Circle – Business Cards</title>
<link href="https://fonts.googleapis.com/css2?family=Nunito+Sans:wght@400;600;700&display=swap" rel="stylesheet">
<style>
  :root {
    --backdrop: #ee9535;
    --ochre: #f5a23a;
    --ink: #1f1f1f;
    --card-edge: #dcdedf;
    --card-light: #ffffff;
    --panel-edge: #ececec;
  }
  * { margin: 0; padding: 0; box-sizing: border-box; }
  html, body { width: 1200px; height: 1000px; overflow: hidden; }
  body {
    position: relative;
    background: var(--backdrop);
    font-family: "Nunito Sans", sans-serif;
    color: var(--ink);
  }
  .card {
    position: absolute;
    left: 258px;
    width: 682px;
    height: 389px;
    background: linear-gradient(180deg, var(--card-edge) 0%, var(--card-light) 50%, var(--card-edge) 100%);
  }
  .card--front { top: 94px; }
  .card--back { top: 514px; }

  .brand {
    position: absolute;
    display: flex;
    align-items: center;
    gap: 10px;
    white-space: nowrap;
    color: var(--ochre);
    font-weight: 600;
  }
  .brand__dot {
    display: block;
    border-radius: 50%;
    background: var(--ochre);
  }
  .card--front .brand {
    left: 0; right: 0; top: 198px;
    justify-content: center;
    font-size: 37px;
    line-height: 1;
  }
  .card--front .brand__dot { width: 22px; height: 22px; }
  .strategy {
    position: absolute;
    left: 0; right: 0; top: 253px;
    text-align: center;
    font-size: 16px;
    font-weight: 600;
    letter-spacing: 1.6px;
  }

  .values {
    position: absolute;
    left: 0; top: 66px;
    width: 268px;
    list-style: none;
  }
  .values__item {
    display: flex;
    justify-content: center;
    align-items: center;
    gap: 5px;
    height: 49px;
    font-size: 17px;
    font-weight: 600;
  }
  .tick { width: 16px; height: 14px; flex: none; }

  .contact-panel {
    position: absolute;
    left: 273px; top: 22px;
    width: 387px; height: 346px;
    border-radius: 8px;
    background: linear-gradient(180deg, var(--panel-edge) 0%, var(--card-light) 45%, var(--panel-edge) 100%);
    box-shadow: 0 2px 14px rgba(0,0,0,0.18);
  }
  .contact-panel .brand {
    left: 0; right: 0; top: 104px;
    justify-content: center;
    font-size: 23px;
    line-height: 1;
    gap: 8px;
  }
  .contact-panel .brand__dot { width: 14px; height: 14px; }
  .person {
    position: absolute;
    right: 19px; top: 162px;
    font-size: 25px;
    font-weight: 600;
  }
  .role-rule {
    position: absolute;
    left: 12px; right: 10px; top: 194px;
    display: flex;
    align-items: center;
    gap: 3px;
    color: var(--ochre);
    font-size: 19px;
    letter-spacing: 1px;
  }
  .role-rule__line { height: 2px; background: var(--ochre); }
  .role-rule__line--long { flex: 1; }
  .role-rule__line--short { width: 12px; }
  .contacts {
    position: absolute;
    left: 13px; top: 219px;
    list-style: none;
  }
  .contacts__item {
    display: flex;
    align-items: center;
    gap: 10px;
    height: 22px;
    font-size: 16px;
    font-weight: 600;
  }
  .icon { width: 18px; height: 16px; flex: none; }
  .address {
    position: absolute;
    left: 13px; top: 292px;
    font-size: 16px;
    line-height: 22px;
    font-weight: 600;
    font-style: normal;
  }
</style>
</head>
<body>

<section class="card card--front">
  <div class="brand"><span class="brand__dot"></span>Homeward Kin Circle</div>
  <p class="strategy">FOCUS: INDIVIDUAL, CULTURAL, SYSTEMIC.</p>
</section>

<section class="card card--back">
  <ul class="values">
    <li class="values__item">One big family <svg class="tick" viewBox="0 0 16 14"><path d="M1 7.5l4.5 4.5L15 1.5" fill="none" stroke="#f5a23a" stroke-width="3" stroke-linecap="round" stroke-linejoin="round"/></svg></li>
    <li class="values__item">Sleep well at night <svg class="tick" viewBox="0 0 16 14"><path d="M1 7.5l4.5 4.5L15 1.5" fill="none" stroke="#f5a23a" stroke-width="3" stroke-linecap="round" stroke-linejoin="round"/></svg></li>
    <li class="values__item">Open heart, open mind <svg class="tick" viewBox="0 0 16 14"><path d="M1 7.5l4.5 4.5L15 1.5" fill="none" stroke="#f5a23a" stroke-width="3" stroke-linecap="round" stroke-linejoin="round"/></svg></li>
    <li class="values__item">If not us, who? <svg class="tick" viewBox="0 0 16 14"><path d="M1 7.5l4.5 4.5L15 1.5" fill="none" stroke="#f5a23a" stroke-width="3" stroke-linecap="round" stroke-linejoin="round"/></svg></li>
    <li class="values__item">Rock solid <svg class="tick" viewBox="0 0 16 14"><path d="M1 7.5l4.5 4.5L15 1.5" fill="none" stroke="#f5a23a" stroke-width="3" stroke-linecap="round" stroke-linejoin="round"/></svg></li>
    <li class="values__item">Do more with less <svg class="tick" viewBox="0 0 16 14"><path d="M1 7.5l4.5 4.5L15 1.5" fill="none" stroke="#f5a23a" stroke-width="3" stroke-linecap="round" stroke-linejoin="round"/></svg></li>
  </ul>

  <div class="contact-panel">
    <div class="brand"><span class="brand__dot"></span>Homeward Kin Circle</div>
    <p class="person">Gary Tolvern</p>
    <div class="role-rule"><span class="role-rule__line role-rule__line--long"></span>CEO<span class="role-rule__line role-rule__line--short"></span></div>
    <ul class="contacts">
      <li class="contacts__item">
        <svg class="icon" viewBox="0 0 18 16"><path d="M2 6c0-3 3-4 7-4s7 1 7 4l-3 1-1-2H6L5 7z" fill="#f5a23a"/><path d="M4 8h10l2 6H2z" fill="#f5a23a"/><circle cx="9" cy="11" r="1.8" fill="#fff"/></svg>
        +61 (0)472 918254
      </li>
      <li class="contacts__item">
        <svg class="icon" viewBox="0 0 18 16"><rect x="1" y="3" width="16" height="11" fill="#f5a23a"/><path d="M1.5 3.5L9 9.5l7.5-6M1.5 13.5l5.5-5M16.5 13.5l-5.5-5" fill="none" stroke="#fff" stroke-width="1.3"/></svg>
        gary.tolvern@homewardkincircle.com
      </li>
      <li class="contacts__item">
        <svg class="icon" viewBox="0 0 18 16"><circle cx="9" cy="8" r="7" fill="#f5a23a"/><path d="M5 4c2 1 1 3 3 3s1 3 0 4M12 3c-1 2 1 3 2 3M11 10c1 0 2 1 2 3" fill="none" stroke="#fff" stroke-width="1.4"/></svg>
        www.homewardkincircle.com
      </li>
    </ul>
    <address class="address">PO Box 8471, Coffs Harbour<br>NSW 2450 Australia</address>
  </div>
</section>

</body>
</html>
```